Fern Assembly Business Cards

Looking or a business card design for my start-up, called "Fern Assembly".
Our tagline is "Growing shared strength for good through learning, teamwork, and service."
Our mission-driven work includes professional/personal development workshops, educational design services, organizational & project management consulting, and coaching services for K-12 schools, organizations, and individuals.
You can check out the website we're building at fernassembly.example
I select projects from designers who are highly responsive to feedback, engage in dialog about revisions, and provide all root/source documents (so please state in your initial submission that you agree to do so).
Looking forward to seeing your great designs!!
Updates
Hello everyone,
Industry/Entity Type
Building
Requirements
Must have
- Looking for a two sided design that includes our logo (I am uploading two variations that I would like incorporated in .ai format) and website on both sides.
The front side must include:
Logo, Name, Title, Phone, Email, Twitter handle
The back side must include: Logo, @fernassem (our organizational twitter handle)
Nice to have
- I like the rounded corner business cards, but that is not absolutely essential.
Should not have
- Colors beyond those presented in our logo.

```html
<!DOCTYPE html>
<html lang="en">
<head>
<meta charset="utf-8">
<title>Fern Assembly Business Cards</title>
<link rel="stylesheet" href="https://fonts.googleapis.com/css2?family=Cormorant+Garamond:wght@500;600&display=swap">
<style>
  :root {
    --backdrop: #d9d9db;
    --card-dark: #0c0c0c;
    --card-light: #ffffff;
    --stone: #a39d96;
    --sky: #5ec4dd;
    --muted-light: #c9c4be;
  }
  * { margin: 0; padding: 0; box-sizing: border-box; }
  html, body { width: 1200px; height: 901px; overflow: hidden; }
  body {
    background: var(--backdrop);
    font-family: "Cormorant Garamond", "Times New Roman", serif;
    position: relative;
  }
  .card {
    position: absolute;
    top: 296px;
    width: 540px;
    height: 309px;
    border-radius: 6px;
    overflow: hidden;
  }
  .card--back { left: 50px; background: var(--card-dark); }
  .card--front { left: 610px; background: var(--card-light); }

  .brand { display: flex; align-items: center; gap: 12px; }
  .brand__dot { width: 22px; height: 22px; border-radius: 50%; background: var(--sky); flex: none; }
  .brand__name {
    color: var(--stone);
    font-weight: 600;
    text-transform: uppercase;
    letter-spacing: 0.04em;
    line-height: 1;
  }

  .card--back .brand { position: absolute; left: 0; right: 0; top: 110px; justify-content: center; }
  .card--back .brand__name { font-size: 34px; }
  .back__tagline {
    position: absolute; left: 0; right: 0; top: 160px;
    text-align: center;
    color: var(--muted-light);
    font-size: 12.5px;
    letter-spacing: 0.12em;
    text-transform: uppercase;
    line-height: 1.35;
  }
  .back__web {
    position: absolute; right: 30px; bottom: 22px;
    color: var(--muted-light);
    font-size: 14px;
  }

  .card--front .brand { position: absolute; left: 34px; top: 70px; }
  .card--front .brand__name { font-size: 27px; }
  .front__pillars {
    position: absolute; left: 68px; top: 104px;
    color: var(--stone);
    font-size: 10.5px;
    letter-spacing: 0.28em;
    text-transform: uppercase;
  }
  .person { position: absolute; right: 44px; top: 72px; text-align: right; text-transform: uppercase; }
  .person__name { color: var(--stone); font-size: 20px; font-weight: 600; letter-spacing: 0.03em; }
  .person__title { color: var(--sky); font-size: 15px; font-weight: 600; letter-spacing: 0.05em; }

  .contact {
    position: absolute; left: 34px; bottom: 8px;
    list-style: none; color: var(--stone);
    font-size: 15px; line-height: 1.5;
  }
  .contact__item { display: flex; align-items: center; gap: 8px; }
  .contact__item--web { margin-top: 20px; }
  .contact__item--web b { font-weight: 600; }
  .contact__icon { width: 11px; height: 11px; flex: none; }

  .edge-strip { position: absolute; top: 0; right: 0; width: 14px; height: 100%; background: var(--stone); }
  .edge-strip__accent { position: absolute; top: 0; right: 0; width: 14px; height: 70px; background: var(--sky); }
  .edge-strip__accent--low { top: 150px; height: 22px; }
</style>
</head>
<body>
  <section class="card card--back" aria-label="Business card back">
    <div class="brand">
      <span class="brand__dot"></span>
      <span class="brand__name">Fern Assembly</span>
    </div>
    <p class="back__tagline">Growing shared strength for good through<br>learning, teamwork, and service</p>
    <p class="back__web">www.fernassembly.example</p>
  </section>

  <section class="card card--front" aria-label="Business card front">
    <div class="brand">
      <span class="brand__dot"></span>
      <span class="brand__name">Fern Assembly</span>
    </div>
    <p class="front__pillars">Learning | Teamwork | Growth</p>

    <div class="person">
      <p class="person__name">Mara Ellison</p>
      <p class="person__title">President</p>
    </div>

    <ul class="contact">
      <li class="contact__item">
        <svg class="contact__icon" viewBox="0 0 12 12" aria-hidden="true"><rect x="3" y="0.5" width="6" height="11" rx="1" fill="none" stroke="#5ec4dd" stroke-width="1.4"/></svg>
        + 0 555 010 199
      </li>
      <li class="contact__item">
        <svg class="contact__icon" viewBox="0 0 12 12" aria-hidden="true"><rect x="0.7" y="2" width="10.6" height="8" fill="none" stroke="#5ec4dd" stroke-width="1.3"/><path d="M1 2.5 6 6.5 11 2.5" fill="none" stroke="#5ec4dd" stroke-width="1.2"/></svg>
        mara@fernassembly.example
      </li>
      <li class="contact__item">
        <svg class="contact__icon" viewBox="0 0 12 12" aria-hidden="true"><rect x="1" y="1" width="10" height="10" fill="#5ec4dd"/></svg>
        @fernassem
      </li>
      <li class="contact__item contact__item--web">
        <svg class="contact__icon" viewBox="0 0 12 12" aria-hidden="true"><circle cx="6" cy="6" r="5" fill="none" stroke="#5ec4dd" stroke-width="1.4"/></svg>
        <span>www.<b>fernassembly</b>.example</span>
      </li>
    </ul>

    <div class="edge-strip">
      <span class="edge-strip__accent"></span>
      <span class="edge-strip__accent edge-strip__accent--low"></span>
    </div>
  </section>
</body>
</html>
```